Virtual Assistant/Online Marketing Business Card/Stationary

I need a professional but modern business card/stationary for my company in Dallas called BrivoLane. BrivoLane is a virtual assistant specializing in online marketing. I would like a unique design that stands out and makes my brand clear. Incorporating the logo is a must and have attached it to this brief.

Target Market(s)

small business owners & entrepreneurs, 35-65

Industry/Entity Type

Business

Contact Information for Business Card

Dorla Finch
dorlafinch@brivolane.biz
(214) 555-0187
brivolane.biz

Font styles to use
Sans Serif

Colors
f04a50
3176b5
9bcb3c

Requirements
Must have
• Colors that match the logo colors. Logo integration

```html
<!DOCTYPE html>
<html lang="en">
<head>
<meta charset="utf-8">
<title>BrivoLane Business Card</title>
<link rel="stylesheet" href="https://fonts.googleapis.com/css2?family=Open+Sans:wght@400;700&family=Roboto:wght@400;700&display=swap">
<style>
  :root {
    --page: #ffffff;
    --frame: #d1d3d4;
    --card-dark: #231f20;
    --ink: #231f20;
    --ink-soft: #3d3b3c;
    --white: #ffffff;
    --brand-red: #f04a50;
    --brand-blue: #3176b5;
    --brand-green: #9bcb3c;
    --silver-light: #f4f4f5;
    --silver-mid: #c5c6c8;
    --silver-dark: #7d7e81;
  }
  * { box-sizing: border-box; margin: 0; padding: 0; }
  html, body {
    width: 1200px;
    height: 440px;
    overflow: hidden;
    background: var(--page);
  }
  .sheet {
    position: absolute;
    left: 12px;
    top: 41px;
    width: 1176px;
    height: 350px;
    background: var(--frame);
  }
  .card {
    position: absolute;
    top: 6px;
    width: 564px;
    height: 338px;
    overflow: hidden;
  }
  .card--front {
    left: 6px;
    background: radial-gradient(ellipse 70% 80% at 52% 58%, var(--silver-light) 0%, var(--silver-mid) 55%, var(--silver-dark) 100%);
  }
  .card--back {
    left: 606px;
    background: var(--card-dark);
  }

  /* straight tri-colour bands */
  .stripes {
    position: absolute;
    left: 0;
    right: 0;
    display: flex;
    flex-direction: column;
  }
  .stripe { display: block; width: 100%; }
  .stripe--green { background: var(--brand-green); }
  .stripe--red { background: var(--brand-red); }
  .stripe--blue { background: var(--brand-blue); }

  .card--front .stripes { bottom: 0; gap: 4px; opacity: 0.55; }
  .card--front .stripe { height: 6px; }
  .card--back .stripes { top: 216px; gap: 14px; opacity: 0.35; }
  .card--back .stripe { height: 20px; }

  .brand {
    position: absolute;
    display: flex;
    align-items: center;
    gap: 12px;
    font-family: "Open Sans", sans-serif;
    font-weight: 700;
    letter-spacing: -0.5px;
    line-height: 1;
  }
  .brand__mark {
    flex: none;
    border-radius: 50%;
    background: var(--brand-red);
  }
  .card--front .brand {
    left: 0;
    right: 0;
    top: 150px;
    justify-content: center;
    font-size: 58px;
    color: var(--ink);
  }
  .card--front .brand__mark { width: 22px; height: 22px; }
  .website {
    position: absolute;
    left: 0;
    right: 0;
    top: 284px;
    text-align: center;
    font-family: "Open Sans", sans-serif;
    font-size: 23px;
    color: var(--ink-soft);
  }
  .card--back .brand {
    left: 24px;
    top: 110px;
    font-size: 50px;
    color: var(--white);
  }
  .card--back .brand__mark { width: 20px; height: 20px; }
  .contact {
    position: absolute;
    right: 22px;
    top: 20px;
    text-align: right;
    font-family: "Roboto", sans-serif;
    color: var(--white);
  }
  .contact__name {
    font-size: 32px;
    font-weight: 400;
    line-height: 1.1;
    letter-spacing: 0.3px;
    text-transform: uppercase;
    margin-bottom: 6px;
  }
  .contact__name strong { font-weight: 700; }
  .contact__line {
    font-size: 12px;
    line-height: 1.35;
    font-style: normal;
  }
</style>
</head>
<body>
  <div class="sheet">
    <section class="card card--front" aria-label="Card front">
      <div class="stripes" aria-hidden="true">
        <span class="stripe stripe--green"></span>
        <span class="stripe stripe--red"></span>
        <span class="stripe stripe--blue"></span>
      </div>
      <div class="brand">
        <span class="brand__mark" aria-hidden="true"></span>
        <span class="brand__name">BrivoLane</span>
      </div>
      <p class="website">brivolane.biz</p>
    </section>

    <section class="card card--back" aria-label="Card back">
      <div class="stripes" aria-hidden="true">
        <span class="stripe stripe--green"></span>
        <span class="stripe stripe--red"></span>
        <span class="stripe stripe--blue"></span>
      </div>
      <div class="brand">
        <span class="brand__mark" aria-hidden="true"></span>
        <span class="brand__name">BrivoLane</span>
      </div>
      <div class="contact">
        <h1 class="contact__name"><strong>Dorla</strong> Finch</h1>
        <address class="contact__line">dorlafinch@brivolane.biz</address>
        <p class="contact__line">(214) 555-0187</p>
      </div>
    </section>
  </div>
</body>
</html>
```